Pizzakarton designen
Sehr angenehmer Kontakt ! Vorschläge wurde prompt umgesetzt - sogar am Wochenende ! So wünscht man sich einen Grafiker
Zielgruppe
Wir sind ein Hotel im höchsten Skigebiet Österreichs (Kühtai) - weiters haben wir eine Pizzeria im Haus und planen ab kommendem Winter auch Pizza auszuliefern - dazu benötigen wir coole Pizza-Kartons - diese sollten von Ihnen gestaltet werden.
Die Seitenlaschen der Pizza-Kartons werden von einem örtlichen Sportgeschäft (Alpinsport Brunnauer) als Werbefläche 'gekauft'. Dessen Homepage ist: www.brettmiete.at
ZUSATZ: Die Pizza-Kartons werden im Digitaldruck erstellt - man kann sich also mit den Farben ruhig 'austoben'
Diese Firma wird die Kartons erstellen - da sieht man Beispiele:
https://www.tellerbox-druck.de/de/
Unsere eigene Homepage vom Hotel ist: www.almgrund-hotel.at
In einem weiteren Schritt würden wir evtl. auch Flyer benötigen. Diese sollten dann natürlich das Design der Pizzakartons wiederspiegeln.
Letztes Jahr hatten wir Flyer wie unter: www.tonis.pizza zu sehen.
Da diese aber fast zu klein waren, würden wir dieses Jahr auf Flyer mit Z-Falz setzen
Bei den Dateien ist einerseits die Druckvorlage des Pizza-Kartons und das Logo der Pizzeria - farblich kann das Logo natürlich geändert werden.
Hab noch ein fertiges Karton-Design dazugefügt - dies dient aber lediglich dazu, damit man weiß wie die Ausrichtung sein muss, damit am Schluss nicht alles Kopf steht (im übrigen - dieses Design gefällt mir nicht wirklich )
Aufgabenstellung
Es gibt eigentlich keine genauen Vorgaben - der Gesamt-Eindruck muss einfach stimmen

```html
<!DOCTYPE html>
<html lang="de">
<head>
<meta charset="utf-8">
<title>Toni's Pizzeria – Gratis Zustellung</title>
<link rel="stylesheet" href="https://fonts.googleapis.com/css2?family=Fredoka:wght@600&family=Fira+Sans+Condensed:wght@400;500&display=swap">
<style>
  :root {
    --rust: #6b3a26;
    --cream: #fbf6dc;
    --teal: #86bf9f;
    --teal-dark: #6fa98a;
    --red: #d91c35;
    --ink: #1f1c1c;
    --ink-soft: #3b3634;
    --yellow: #f8d66d;
    --brown: #5a4a3f;
  }
  html, body {
    margin: 0;
    padding: 0;
    width: 1193px;
    height: 1200px;
    overflow: hidden;
    background: #ffffff;
  }
  .sign {
    display: block;
    width: 1193px;
    height: 1200px;
  }
  .headline { font-family: "Fredoka", sans-serif; font-weight: 600; }
  .copy { font-family: "Fira Sans Condensed", sans-serif; }
  .brand-name { font-family: "Fira Sans Condensed", sans-serif; font-weight: 500; fill: var(--brown); }
</style>
</head>
<body>
<svg class="sign" viewBox="0 0 1193 1200" xmlns="http://www.w3.org/2000/svg">
  <defs>
    <radialGradient id="pizza-tone" cx="50%" cy="50%" r="60%">
      <stop offset="0%" stop-color="#d9662f"/>
      <stop offset="70%" stop-color="#c8502a"/>
      <stop offset="100%" stop-color="#e29a4c"/>
    </radialGradient>
    <radialGradient id="garnish-tone" cx="45%" cy="35%" r="65%">
      <stop offset="0%" stop-color="#d92a1e"/>
      <stop offset="65%" stop-color="#b8201a"/>
      <stop offset="100%" stop-color="#3f8a2c"/>
    </radialGradient>
    <linearGradient id="emblem-tone" x1="0" y1="0" x2="0" y2="1">
      <stop offset="0%" stop-color="var(--ink-soft)"/>
      <stop offset="100%" stop-color="var(--ink)"/>
    </linearGradient>
  </defs>

  <!-- sign plate -->
  <rect class="plate-edge" x="6" y="6" width="1181" height="1188" rx="22" fill="var(--rust)"/>
  <rect class="plate-rim" x="14" y="14" width="1165" height="1172" rx="18" fill="var(--cream)"/>
  <rect class="plate-field" x="38" y="40" width="1117" height="1120" rx="10" fill="var(--teal)"/>
  <circle cx="20" cy="20" r="4" fill="var(--cream)"/>
  <circle cx="1173" cy="20" r="4" fill="var(--cream)"/>
  <circle cx="20" cy="1180" r="4" fill="var(--cream)"/>
  <circle cx="1173" cy="1180" r="4" fill="var(--cream)"/>

  <!-- ski emblem circle -->
  <circle class="emblem-ring" cx="615" cy="262" r="182" fill="var(--cream)"/>
  <circle cx="615" cy="262" r="172" fill="none" stroke="var(--teal)" stroke-width="6"/>
  <rect class="emblem-illustration" role="img" aria-label="Illustration: zwei Ski mit Skistöcken vor schneebedeckten Berggipfeln"
    x="470" y="125" width="632" height="255" rx="14" fill="url(#emblem-tone)"/>

  <!-- delivery panel -->
  <polygon class="delivery-panel" points="522,382 1103,304 1094,659 534,606" fill="var(--ink)"/>
  <polygon points="540,396 1088,322 1080,642 549,592" fill="none" stroke="var(--teal)" stroke-width="5"/>
  <text class="headline" x="587" y="470" font-size="68" fill="var(--yellow)" transform="rotate(2 587 470)">GRATIS</text>
  <text class="headline" x="585" y="545" font-size="86" fill="var(--yellow)" transform="rotate(2 585 545)" textLength="450" lengthAdjust="spacingAndGlyphs">ZUSTELLUNG</text>
  <text class="copy" x="587" y="573" font-size="20" fill="var(--yellow)" transform="rotate(2 587 573)">* ab einer Bestellung von € 20,-</text>

  <!-- Pizzeria banner -->
  <polygon class="pizzeria-banner" points="87,124 435,205 429,304 84,255" fill="var(--red)"/>
  <text class="headline" x="106" y="238" font-size="78" fill="var(--cream)" transform="rotate(9 106 238)" textLength="300" lengthAdjust="spacingAndGlyphs">Pizzeria</text>

  <!-- restaurant name panel -->
  <polygon class="name-panel-frame" points="68,289 522,335 541,659 174,724" fill="var(--cream)"/>
  <polygon points="90,308 504,350 522,645 188,705" fill="var(--teal)"/>
  <polygon class="name-panel" points="102,318 496,358 512,636 196,693" fill="var(--cream)"/>
  <text class="brand-name" x="318" y="570" font-size="112" text-anchor="middle" transform="rotate(-6 318 570)">TONI'S</text>
  <text class="brand-name" x="330" y="638" font-size="34" letter-spacing="6" text-anchor="middle" transform="rotate(-6 330 638)">RESTAURANT</text>

  <!-- order panel -->
  <polygon class="order-frame" points="68,792 486,713 410,1068 82,1000" fill="var(--cream)"/>
  <polygon points="78,797 468,726 398,1054 90,988" fill="var(--teal)"/>
  <polygon class="order-panel" points="84,808 453,739 388,1044 96,969" fill="var(--red)"/>
  <g class="copy" fill="var(--cream)" transform="rotate(5 134 838)">
    <text x="134" y="838" font-size="30">Bestell-Hotline</text>
    <text x="134" y="874" font-size="30">+43 5200 1847</text>
    <text x="134" y="930" font-size="30">Online-Bestellung</text>
    <text x="134" y="964" font-size="28" letter-spacing="1">www.tonis.pizza</text>
  </g>

  <!-- pizza circle -->
  <circle class="pizza-ring" cx="850" cy="922" r="204" fill="var(--cream)"/>
  <circle cx="850" cy="922" r="193" fill="none" stroke="var(--teal)" stroke-width="6"/>
  <ellipse class="pizza-photo" role="img" aria-label="Foto: Salamipizza mit Rucola, in Stücke geschnitten"
    cx="855" cy="925" rx="262" ry="172" transform="rotate(-8 855 925)" fill="url(#pizza-tone)"/>
  <ellipse class="garnish-photo" role="img" aria-label="Foto: Rispentomaten und frisches Basilikum"
    cx="580" cy="950" rx="112" ry="148" fill="url(#garnish-tone)"/>
</svg>
</body>
</html>
```